LANDING PAGE DESIGN - MONEY GUARANTEED & 2ND PLACE PAYOUT

brightlanework.net
Top Slide
Are you interested in earning from $65,000.00 - $91,000.00 a year from home?
NO PREVIOUS MARKETING EXPERIENCE NEEDED
---- scene 2 of slide --- please provide nice graphical images along with the text on each slide --
We are looking for motivated individuals from “GEO IP” with to join our team.
Qualify below to earn $100.00 a day while u learn to make $$
---Please don’t forget to create both slides when u post your design ---
Who should apply?
Anyone from the age of 18-65 who has at least 6 months experience using Chatterloop and or Swapboard. There is no marketing experience necessary or required and no background checks will be ran. The only really requirements are a home computer and internet connection and the ability to follow simple directions.

__featured jobs section__ Please make this section feature the 2 current available positions we are hiring for
Available Positions – Chatterloop AD Specialist –
Enroll in an 8 week training class that pays you $500.00 per week.
Training takes about 30-60 minutes a day 5 days a week for 8 weeks. Make $100.00 a day during training, and $250.00 a day 5-7 days a week after training is complete.
What do we do?
Help small businesses sale products through social media channels like Chatterloop & Pictavo. Our customers primary focus on the health and beauty niche.
Swapboardz Post Specialist
Enroll in a 6 weeks training that pays you $25.00 per day. Earn $100.00 a day after successfully completing your training. Course requires 30 minutes per day at least 3 times per week.
What do we do?
We help local real estate brokers, insurance agents, and other small businesses grow their businesses through targeted classified ad posting all over the country.

How do you apply?

First you must fill out our short application.
(Create an iframe - Frame #1)
First Name, Last Name, Age, City, State, Zip, Phone, Email
(Frame #2)
Do you have a desktop or laptop computer?
Do you have 24/7 access to the internet?
Are you at least 18 years old?
Do you have Photo ID? (must match your Chatterloop name)
Are you ready to start making money immediately?
(end of frames)

Testimonials Section
Leave space/frame for 3 video testimonials

Get Paid Referring Friends (need someway to track / pay for referrals)
We will pay you $5.00 for every qualified friend that you refer to us. Fill out the application above to get more information on our referral program.

After they complete the application I would like them to be sent an email saying that they qualify for both positions but we don’t have training agents available until “random day 2-3 months ahead”
BUT YOU QUALIFY FOR OUR SECONDARY OFFER
Would you like to earn $100.00 today – and up to $150.00 a week while getting a jump start on your training? “they click yes or no” when they click yes – it would take them to another page which explains to them to download TeamViewer so we can run ads from their CL promoting our partners and we will pay them weekly for it.

Target Market(s)

Lower Income Users Looking to make $$ from home who have an active Chatterloop account as well as a home computer and high speed internet.

Industry/Entity Type

Marketing

Number of Pages Required

1 page

Requirements
Must have
• This is a landing page / lead capturing page - So please make sure that the site focuses on pushing the user to enter their contact details and submit our qualifier form.
Nice to have
• I've always like the more cartoony websites - but must still be clean/professional looking with proper use of the fold of the page and whitespaces.

```html
<!DOCTYPE html>
<html lang="en">
<head>
<meta charset="utf-8">
<title>BrightLaneWork – Work From Home</title>
<link rel="stylesheet" href="https://fonts.googleapis.com/css2?family=Montserrat:wght@300;400;600;700;800&family=Patua+One&display=swap">
<style>
:root{
  --blue:#0a70bd;
  --blue-card:#2e93d8;
  --blue-card-dark:#2a7bb8;
  --purple:#a932d3;
  --purple-dark:#8a2db0;
  --orange:#f7941d;
  --red:#e8321c;
  --red-light:#f25a22;
  --navy:#2c2d42;
  --field:#3590d5;
  --green:#3bb54a;
  --grey:#e6e6e6;
  --text-dark:#333;
  --white:#fff;
}
*{box-sizing:border-box;margin:0;padding:0}
html,body{width:1200px;height:2990px;overflow:hidden}
body{font-family:"Montserrat",sans-serif;color:var(--text-dark);background:var(--white);position:relative}
.abs{position:absolute}

/* hero */
.hero{position:absolute;left:0;top:0;width:1200px;height:676px;background:var(--blue)}
.brand{left:60px;top:32px;font-family:"Patua One",serif;font-size:28px;color:#fff}
.nav-contact{left:876px;top:44px;font-size:18px;font-weight:700;color:#fff}
.nav-join{left:988px;top:38px;width:88px;height:38px;border:2px solid #fff;color:#fff;font-size:17px;font-weight:700;display:flex;align-items:center;justify-content:center}
.hero-title{left:60px;top:148px;width:624px;text-align:center;color:#fff;font-size:44px;font-weight:300;line-height:52px}
.hero-sub{left:60px;top:356px;width:624px;text-align:center;color:#fff;font-size:44px;font-weight:300;line-height:52px}
.hero-btn{left:330px;top:554px;width:158px;height:42px;background:var(--orange);color:#fff;font-weight:700;font-size:17px;display:flex;align-items:center;justify-content:center}
.hero-art{left:720px;top:180px;width:430px;height:420px;border-radius:40% 40% 20% 20%;background:radial-gradient(circle at 50% 40%,#2c3d52,#0a5e9e 75%)}

/* who */
.who{position:absolute;left:0;top:676px;width:1200px;height:306px;background:linear-gradient(90deg,var(--red),var(--red-light) 50%,var(--red))}
.who-art{left:0;top:0;width:580px;height:306px;background:linear-gradient(180deg,rgba(255,255,255,0) 0%,#4a5fa8 55%,#3a4a8a 100%)}
.who-title{left:644px;top:64px;font-size:32px;color:#fff}
.who-text{left:644px;top:106px;width:436px;font-size:16.5px;line-height:22px;color:#fff;text-align:justify}

/* jobs */
.jobs-title{left:0;top:990px;width:1200px;text-align:center;font-size:32px;font-weight:300;color:#777}
.card{top:1052px;width:444px;height:518px;color:#fff;text-align:center}
.card-blue{left:140px;background:var(--blue-card)}
.card-purple{left:620px;background:var(--purple)}
.card-head{height:62px;display:flex;align-items:center;justify-content:center;font-weight:700;font-size:17px}
.card-blue .card-head,.card-blue .card-foot{background:var(--blue-card-dark)}
.card-purple .card-head,.card-purple .card-foot{background:var(--purple-dark)}
.card-body{padding:14px 44px 0;font-size:17px;line-height:22px}
.card-body p{margin-bottom:8px}
.card-body .gap{margin-top:28px;margin-bottom:0}
.card-foot{position:absolute;left:0;bottom:0;width:100%;height:50px;display:flex;align-items:center;justify-content:center;font-weight:700;font-size:16px;color:rgba(255,255,255,.55);border-top:2px solid rgba(0,0,0,.2)}
.view-all{left:494px;top:1588px;width:212px;height:40px;background:var(--orange);color:#fff;font-size:17px;display:flex;align-items:center;justify-content:center}

/* apply */
.apply{position:absolute;left:0;top:1636px;width:1200px;height:568px;background:var(--navy)}
.apply-title{left:90px;top:108px;font-size:32px;font-weight:700;color:#fff}
.apply-sub{left:90px;top:148px;font-size:17px;color:#fff}
.field{height:40px;background:var(--field);color:#fff;font-size:18px;padding-left:10px;display:flex;align-items:center}
.quiz{left:640px;top:184px;width:498px;height:276px;background:var(--green);color:#fff;font-size:17px}
.q{position:absolute;left:28px;display:flex;align-items:flex-start;gap:18px;width:450px;line-height:21px}
.q i{flex:0 0 20px;height:20px;background:var(--navy);border-radius:3px;margin-top:1px}

/* testimonials */
.say{left:0;top:2270px;width:1200px;text-align:center;font-size:16px;color:#444;letter-spacing:.5px}
.video{top:2352px;width:310px;height:216px;border:4px solid #4a84c9;border-radius:4px;background:#fff;overflow:hidden}
.video-bar{height:22px;background:#4a84c9}
.video-scene{position:absolute;left:0;top:22px;width:100%;height:190px;background:linear-gradient(180deg,#fff,#e9eef5)}
.video-prog{position:absolute;left:14px;bottom:22px;width:274px;height:6px;border-radius:3px;background:#4a84c9}
.video-prog span{display:block;width:70px;height:100%;border-radius:3px;background:#e84a5f}

/* referral */
.refer-left{left:0;top:2700px;width:524px;height:100px;background:linear-gradient(90deg,var(--red),var(--red-light));color:#fff;text-align:center}
.refer-left b{display:block;margin-top:20px;font-size:36px;font-weight:800;line-height:38px}
.refer-left span{font-size:18px}
.refer-right{left:524px;top:2700px;width:676px;height:100px;background:#000;color:#fff;font-size:17px;line-height:21px;padding:14px 40px 0 40px}

/* footer */
.footer{position:absolute;left:0;top:2804px;width:1200px;height:186px;background:var(--grey)}
.foot-mark{left:80px;top:40px;width:104px;height:104px;border-radius:50%;border:6px solid #666}
.foot-title{left:208px;top:48px;font-size:32px;color:#555}
.foot-text{left:208px;top:88px;width:400px;font-size:16px;line-height:19px;color:#555}
.social{top:82px;display:flex;align-items:center;gap:10px;font-size:17px;font-weight:600;color:#333}
.social i{width:26px;height:26px;border-radius:50%;display:block}
.copy{left:960px;top:154px;width:180px;text-align:right;font-size:16px;color:#555}
</style>
</head>
<body>

<section class="hero">
  <div class="abs brand">BrightLaneWork</div>
  <div class="abs nav-contact">Contact</div>
  <div class="abs nav-join">JOIN</div>
  <h1 class="abs hero-title" style="font-weight:300">We are looking for motivated individuals from “GEO IP” to join our team.</h1>
  <p class="abs hero-sub">Qualify below to earn $100.00 a day while u learn to make $$</p>
  <div class="abs hero-btn">APPLY NOW</div>
  <div class="abs hero-art" role="img" aria-label="Cartoon businessman opening his shirt to reveal a superhero emblem"></div>
</section>

<section class="who">
  <div class="abs who-art" role="img" aria-label="Cartoon man working on a laptop while sitting on a sofa"></div>
  <h2 class="abs who-title" style="font-weight:400">Who should apply?</h2>
  <p class="abs who-text">Anyone from the age of 18-65 who has at least 6 months experience using Chatterloop and or Swapboard. There is no marketing experience necessary or required and no background checks will be ran. The only really requirements are a home computer and internet connection and the ability to follow simple directions.</p>
</section>

<h2 class="abs jobs-title">Featured Jobs</h2>

<article class="abs card card-blue">
  <div class="card-head">Chatterloop AD Specialist</div>
  <div class="card-body">
    <p>Enroll in an 8 week training class that pays you $500.00 per week.</p>
    <p>Training takes about 30-60 minutes a day 5 days a week for 8 weeks.</p>
    <p>Make $100.00 a day during training, and $250.00 a day 5-7 days a week after training is complete.</p>
    <p class="gap">What do we do?</p>
    <p>Help small businesses sale products through social media channels like Chatterloop &amp; Pictavo. Our customers primary focus on the health and beauty niche.</p>
  </div>
  <div class="card-foot">APPLY</div>
</article>

<article class="abs card card-purple">
  <div class="card-head">Swapboardz Post Specialist</div>
  <div class="card-body">
    <p>Enroll in a 6 weeks training that pays you $25.00 per day.</p>
    <p>Earn $100.00 a day after successfully completing your training.</p>
    <p>Course requires 30 minutes per day at least 3 times per week.</p>
    <p class="gap">What do we do?</p>
    <p>We help local real estate brokers, insurance agents, and other small businesses grow their businesses through targeted classified ad posting all over the country.</p>
  </div>
  <div class="card-foot">APPLY</div>
</article>

<div class="abs view-all">View all Jobs</div>

<section class="apply">
  <h2 class="abs apply-title">How to Apply?</h2>
  <p class="abs apply-sub">First you must fill out our short application.</p>
  <div class="abs field" style="left:90px;top:200px;width:246px">First Name</div>
  <div class="abs field" style="left:364px;top:200px;width:248px">Last Name</div>
  <div class="abs field" style="left:90px;top:270px;width:108px">Age</div>
  <div class="abs field" style="left:236px;top:270px;width:376px">Phone</div>
  <div class="abs field" style="left:90px;top:334px;width:246px">Email</div>
  <div class="abs field" style="left:364px;top:334px;width:248px">City</div>
  <div class="abs field" style="left:90px;top:400px;width:246px">State</div>
  <div class="abs field" style="left:364px;top:400px;width:248px">Zip</div>
  <div class="abs quiz">
    <div class="q" style="top:26px"><i></i>Do you have a desktop or laptop computer?</div>
    <div class="q" style="top:64px"><i></i>Do you have 24/7 access to the internet?</div>
    <div class="q" style="top:104px"><i></i>Are you at least 18 years old?</div>
    <div class="q" style="top:146px"><i></i>Do you have Photo ID? (must match your Chatterloop name)</div>
    <div class="q" style="top:208px"><i></i>Are you ready to start making money immediately?</div>
  </div>
</section>

<p class="abs say">WHAT PEOPLE ARE SAYING</p>

<div class="abs video" style="left:62px">
  <div class="video-bar"></div>
  <div class="video-scene" role="img" aria-label="Video testimonial from a happy team member"></div>
  <svg class="abs" style="left:103px;top:42px" width="96" height="96" viewBox="0 0 96 96"><circle cx="48" cy="48" r="42" fill="none" stroke="#4a84c9" stroke-width="8"/><path d="M38 28 L70 48 L38 68 Z" fill="#2e93d8"/></svg>
  <div class="video-prog"><span></span></div>
</div>
<div class="abs video" style="left:446px">
  <div class="video-bar"></div>
  <div class="video-scene" role="img" aria-label="Video testimonial from a happy team member"></div>
  <svg class="abs" style="left:103px;top:42px" width="96" height="96" viewBox="0 0 96 96"><circle cx="48" cy="48" r="42" fill="none" stroke="#4a84c9" stroke-width="8"/><path d="M38 28 L70 48 L38 68 Z" fill="#2e93d8"/></svg>
  <div class="video-prog"><span></span></div>
</div>
<div class="abs video" style="left:828px">
  <div class="video-bar"></div>
  <div class="video-scene" role="img" aria-label="Video testimonial from a happy team member"></div>
  <svg class="abs" style="left:103px;top:42px" width="96" height="96" viewBox="0 0 96 96"><circle cx="48" cy="48" r="42" fill="none" stroke="#4a84c9" stroke-width="8"/><path d="M38 28 L70 48 L38 68 Z" fill="#2e93d8"/></svg>
  <div class="video-prog"><span></span></div>
</div>

<div class="abs refer-left"><b>Earn $5</b><span>Refer a friend</span></div>
<div class="abs refer-right">We will pay you $5.00 for every qualified friend that you refer to us. Fill out the application above to get more information on our referral program.</div>

<footer class="footer">
  <div class="abs foot-mark"></div>
  <h3 class="abs foot-title" style="font-weight:400">Follow Us</h3>
  <p class="abs foot-text">We are about to launch! Follow us to get notified about BrightLaneWork latest news and updates.</p>
  <div class="abs social" style="left:700px"><i style="background:#3b5a9a"></i>Chatterloop</div>
  <div class="abs social" style="left:870px"><i style="background:#2ea4dc"></i>Chirpline</div>
  <div class="abs social" style="left:1020px"><i style="background:#d6458a"></i>Pictavo</div>
  <p class="abs copy">Copyright 2017</p>
</footer>

</body>
</html>
```